Psychiatric Office Needs a Website- 1st Time Ever!

Been in practice since 2003 with no website, but finally ready to dive in. We are Maplecrest Behavioral Healthcare, a mental health outpatient practice based in Fayetteville, Georgia that sees diverse individuals and families from childhood to advanced age for a variety of conditions. We've grown by word of mouth and referral but would now like to have a digital footprint. Be the pioneer of our website and we will be sure to share. We would like to see designs that are modern, animated, fairly colorful, easy to read, and caters to all ages. Also, we would like the design to take the whole page (not be centered) and can be viewed well on phone/tablet. Please see our outline for more information. Our motto/slogan is: Maplecrest Behavioral Healthcare- A step forward in your wellness journey, so the design should try to reflect that.
Updates

Target Market(s)

Children through elderly

Industry/Entity Type

Medical

Logo Text

Stepping forward in your wellness journey

Number of Pages Required

1 page

Colors

Designer to choose colors to be used in the design.

Requirements
Must have
• Animation or moving pictures.
• Color.
• Concise.
• User friendly
• Diversity in the stock photos

```html
<!DOCTYPE html>
<html lang="en">
<head>
<meta charset="utf-8">
<title>Maplecrest Behavioral Healthcare</title>
<link rel="stylesheet" href="https://fonts.googleapis.com/css2?family=Cabin:wght@400;500;600;700&display=swap">
<style>
:root{
  --navy:#0d5a80;
  --navy-dark:#0a4a6b;
  --sky:#4fb3e6;
  --cyan:#1fb5d6;
  --band:#0b6593;
  --ink:#333b42;
  --muted:#6b7177;
  --card:#f5f5f5;
  --line:#e3e3e3;
  --footer:#2f2f2f;
  --footer-text:#c9c9c9;
  --white:#ffffff;
}
*{box-sizing:border-box;margin:0;padding:0}
html,body{width:1200px;height:2835px;overflow:hidden;background:var(--white)}
body{font-family:"Cabin",sans-serif;color:var(--ink);position:relative}
a{color:inherit;text-decoration:none}
.abs{position:absolute}

/* Header */
.site-header{position:absolute;left:0;top:0;width:1200px;height:127px;background:var(--white)}
.brand{position:absolute;left:157px;top:26px;display:flex;align-items:center;gap:10px;color:var(--navy);font-weight:600;font-size:14px;line-height:1.15;width:140px}
.brand-mark{width:44px;height:44px;border-radius:50%;background:var(--navy);flex:none}
.topbar{position:absolute;top:26px;left:760px;display:flex;align-items:center;gap:12px;font-size:14px}
.topbar .call{color:var(--navy);font-weight:700;display:flex;align-items:center;gap:6px}
.topbar .call span{font-weight:400;color:var(--sky)}
.social-dot{width:22px;height:22px;border-radius:50%;background:#b9bec2;margin-left:26px}
.login{color:var(--navy);font-weight:600;display:flex;align-items:center;gap:5px}
.main-nav{position:absolute;top:72px;left:302px;display:flex;align-items:center;font-size:13.5px;color:var(--ink)}
.main-nav a{margin-right:0}
.nav-home{color:var(--sky);position:absolute;left:4px}
.nav-about{position:absolute;left:68px}
.nav-services{position:absolute;left:170px}
.nav-conditions{position:absolute;left:248px;white-space:nowrap}
.nav-patients{position:absolute;left:395px;white-space:nowrap}
.nav-contact{position:absolute;left:501px}
.btn{display:inline-flex;align-items:center;justify-content:center;border-radius:18px;font-size:13px;font-weight:500;color:var(--white);background:var(--navy)}
.btn-header{position:absolute;left:875px;top:68px;width:168px;height:35px;background:var(--navy-dark);font-size:13.5px}

/* Hero */
.hero{position:absolute;left:0;top:127px;width:1200px;height:433px;overflow:hidden}
.hero-photo{position:absolute;inset:0;background:linear-gradient(100deg,#9aa3ad 0%,#c2c8ce 30%,#d8dde1 55%,#b9c7cf 75%,#8fb6c4 100%)}
.hero-shade{position:absolute;inset:0;background:linear-gradient(90deg,rgba(60,70,80,.35) 0%,rgba(60,70,80,.05) 55%,rgba(0,0,0,0) 100%)}
.hero-title{position:absolute;left:157px;top:130px;width:580px;color:var(--white);font-size:28px;font-weight:500;line-height:1.25}
.hero-actions{position:absolute;left:157px;top:259px;display:flex;gap:28px}
.hero-actions .btn{height:34px;font-size:13px}
.btn-screening{width:140px;background:var(--navy-dark)}
.btn-appoint{width:150px;background:var(--sky)}
.hero-arrow{position:absolute;top:195px;width:24px;height:40px}
.hero-arrow.prev{left:58px}
.hero-arrow.next{left:1122px}

/* About */
.about-photo{position:absolute;left:210px;top:608px;width:328px;height:320px;background:linear-gradient(135deg,#e8dccf 0%,#d2b49a 45%,#b6937a 100%)}
.about-body{position:absolute;left:588px;top:640px;width:404px}
.eyebrow{font-size:12px;color:var(--ink)}
.section-heading{font-size:22px;font-weight:600;color:var(--navy);display:flex;align-items:center;gap:22px;white-space:nowrap}
.section-heading::after{content:"";display:block;height:2px;background:var(--navy)}
.about-body .section-heading::after{width:160px}
.about-lead{margin-top:30px;font-size:13.5px;line-height:1.45;color:var(--ink)}
.about-text{margin-top:22px;font-size:11.5px;line-height:1.5;color:var(--muted)}
.text-link{display:inline-block;margin-top:22px;font-size:12.5px;color:var(--sky);border-bottom:1px solid var(--sky);padding-bottom:2px}

/* Shared headings */
.block-heading{position:absolute;left:157px}
.block-heading::after{width:205px}
.pager{position:absolute;display:flex;gap:8px}
.pager span{width:22px;height:22px;border-radius:50%;display:flex;align-items:center;justify-content:center}
.pager .prev{border:1.5px solid var(--cyan);background:var(--white)}
.pager .next{background:var(--cyan)}

/* Services */
.service-card{position:absolute;top:1058px;width:280px;height:390px;background:var(--card);border-bottom:2px solid var(--line)}
.service-photo{height:172px;border-bottom:6px solid var(--navy)}
.service-card h3{margin:20px 24px 0;font-size:17px;font-weight:500;line-height:1.45;color:var(--ink);height:52px}
.service-card p{margin:14px 24px 0;font-size:11.5px;line-height:1.5;color:var(--muted)}
.service-card .btn{position:absolute;left:24px;top:331px;width:82px;height:32px;font-size:12.5px}
.service-card .btn.is-active{background:var(--sky)}
.btn-viewall{position:absolute;left:545px;top:1480px;width:110px;height:33px;font-size:12.5px}

/* Conditions */
.conditions{position:absolute;left:0;top:1578px;width:1200px;height:382px;background:linear-gradient(120deg,#0a5f8b 0%,#0b6a98 50%,#095b85 100%)}
.conditions-photo{position:absolute;left:208px;top:0;width:327px;height:382px;background:linear-gradient(160deg,#e9ddd2 0%,#cdb7a3 50%,#a88f7d 100%)}
.conditions-body{position:absolute;left:588px;top:48px;color:var(--white)}
.conditions-body .section-heading{color:var(--white)}
.conditions-body .section-heading::after{width:140px;background:var(--white);height:1.5px}
.condition-list{list-style:none;margin-top:34px}
.condition-list li{display:flex;align-items:center;gap:14px;font-size:18px;height:40.5px}
.btn-conditions{margin-top:18px;width:142px;height:32px;background:var(--sky);font-size:12.5px}

/* News */
.news-item{position:absolute;top:2090px;width:280px}
.news-photo{height:176px}
.news-date{margin-top:30px;font-size:12px;font-weight:700;color:var(--ink)}
.news-title{margin-top:8px;font-size:18.5px;line-height:1.4;color:var(--ink)}
.news-title.is-hover{color:var(--navy);text-decoration:underline;text-underline-offset:3px}
.btn-news{position:absolute;left:545px;top:2390px;width:110px;height:33px;background:var(--sky);font-size:12.5px}

/* Footer */
.site-footer{position:absolute;left:0;top:2487px;width:1200px;height:348px;background:var(--footer);color:var(--footer-text)}
.footer-mark{position:absolute;left:157px;top:64px;width:94px;height:94px;border-radius:50%;background:#ececec}
.footer-contact{position:absolute;left:284px;top:66px;width:270px}
.footer-contact h4{font-size:14px;color:var(--white);font-weight:600}
.footer-contact .addr{margin-top:14px;font-size:11.5px;line-height:1.5}
.footer-contact h5{margin-top:14px;font-size:14px;color:var(--white);font-weight:600}
.footer-contact .phone{font-size:17px;color:var(--white);margin-top:2px}
.footer-contact .mail{font-size:11.5px}
.follow{margin-top:22px;display:flex;align-items:center;gap:10px;font-size:14px;color:var(--white);font-weight:600}
.follow span{width:20px;height:20px;border-radius:50%;background:#bcbcbc}
.quick-links{position:absolute;left:595px;top:66px}
.quick-links h4{font-size:14px;color:var(--white);font-weight:600}
.quick-links ul{list-style:none;margin-top:12px}
.quick-links li{font-size:11.5px;height:27px}
.quick-links li.is-current{color:var(--sky)}
.policy-links{position:absolute;left:764px;top:64px;list-style:none}
.policy-links li{font-size:11.5px;height:26.5px}
.badge{position:absolute;left:962px;top:56px;width:80px;height:90px;border:1.5px solid #bdbdbd;border-radius:6px}
.footer-rule{position:absolute;left:764px;top:175px;width:280px;height:1px;background:#4c4c4c}
.hours{position:absolute;left:764px;top:186px;width:290px}
.hours h4{font-size:14px;color:var(--white);font-weight:600}
.hours p{margin-top:8px;font-size:11.5px;line-height:1.4}
.footer-bottom{position:absolute;left:136px;top:303px;width:928px;height:1px;background:#4c4c4c}
.copyright{position:absolute;left:276px;top:318px;font-size:11.5px}
.to-top{position:absolute;left:996px;top:312px}
</style>
</head>
<body>

<header class="site-header">
  <a class="brand" href="#"><span class="brand-mark"></span><span>Maplecrest Behavioral Healthcare</span></a>
  <div class="topbar">
    <span class="call">Call:
      <svg width="18" height="18" viewBox="0 0 24 24"><circle cx="12" cy="12" r="11" fill="none" stroke="#0d5a80" stroke-width="2"/><path d="M8 6.5c.6-.5 1.4-.4 1.8.2l1 1.6c.3.5.2 1.1-.2 1.5l-.7.6c.6 1.4 1.6 2.4 3 3l.6-.7c.4-.4 1-.5 1.5-.2l1.6 1c.6.4.7 1.2.2 1.8-.9 1-2.3 1.4-3.6.8-2.8-1.2-5-3.4-6.2-6.2-.5-1.3-.1-2.6 1-3.4z" fill="#0d5a80"/></svg>
      <span>+1 404-555-0186</span></span>
    <span class="social-dot"></span>
    <span class="login"><svg width="15" height="15" viewBox="0 0 24 24"><circle cx="12" cy="12" r="10.5" fill="none" stroke="#0d5a80" stroke-width="2"/><circle cx="12" cy="9.5" r="3.5" fill="#0d5a80"/><path d="M5.5 18.5c1.5-2.6 3.8-3.8 6.5-3.8s5 1.2 6.5 3.8" fill="#0d5a80"/></svg>Login</span>
  </div>
  <nav class="main-nav">
    <a class="nav-home" href="#">Home</a>
    <a class="nav-about" href="#">About Us &#8964;</a>
    <a class="nav-services" href="#">Services</a>
    <a class="nav-conditions" href="#">Conditions We Treat</a>
    <a class="nav-patients" href="#">New Patients</a>
    <a class="nav-contact" href="#">Contact</a>
  </nav>
  <a class="btn btn-header" href="#">Make An Appointment</a>
</header>

<section class="hero">
  <div class="hero-photo" role="img" aria-label="Photo of a caregiver smiling with an elderly woman in a wheelchair in a bright living room"></div>
  <div class="hero-shade"></div>
  <h1 class="hero-title">We provide mental health services to children, adults, and the developmentally disabled population</h1>
  <div class="hero-actions">
    <a class="btn btn-screening" href="#">Take a Screening</a>
    <a class="btn btn-appoint" href="#">Make An Appointment</a>
  </div>
  <svg class="hero-arrow prev" viewBox="0 0 24 40"><path d="M20 2 4 20l16 18" fill="none" stroke="#fff" stroke-width="2.5"/></svg>
  <svg class="hero-arrow next" viewBox="0 0 24 40"><path d="M4 2l16 18L4 38" fill="none" stroke="#fff" stroke-width="2.5"/></svg>
</section>

<section class="about">
  <div class="about-photo" role="img" aria-label="Photo of a smiling family with two young children sitting together at home"></div>
  <div class="about-body">
    <p class="eyebrow">About Us</p>
    <h2 class="section-heading">Our Vision &amp; Mission</h2>
    <p class="about-lead">To be the leading provider of outpatient psychiatric care in Atlanta Metro South, working together to promote (the) mental wellness of our community.</p>
    <p class="about-text">To provide mental health services to children, adults, and the developmentally disabled population that is culturally sensitive regardless of age, race, gender, orientation, religion, or creed...</p>
    <a class="text-link" href="#">Discover More About</a>
  </div>
</section>

<section class="services">
  <h2 class="section-heading block-heading" style="top:988px">Our Services</h2>
  <div class="pager" style="left:991px;top:990px">
    <span class="prev"><svg width="8" height="8" viewBox="0 0 8 8"><path d="M6 0 1 4l5 4z" fill="#1fb5d6"/></svg></span>
    <span class="next"><svg width="8" height="8" viewBox="0 0 8 8"><path d="M2 0l5 4-5 4z" fill="#fff"/></svg></span>
  </div>
  <article class="service-card" style="left:157px">
    <div class="service-photo" role="img" aria-label="Photo of a clinician comforting a child lying in a hospital bed" style="background:linear-gradient(135deg,#c9d3d8,#9fb0b8)"></div>
    <h3>Diagnostic evaluation and treatment</h3>
    <p>To provide mental health services to children, adults, and the developmental-ly disabled population...</p>
    <a class="btn" href="#">More</a>
  </article>
  <article class="service-card" style="left:459px">
    <div class="service-photo" role="img" aria-label="Photo of a distressed woman holding her head in her hands" style="background:linear-gradient(135deg,#d8cfc6,#a99a8e)"></div>
    <h3>Psychopharmacology</h3>
    <p>To provide mental health services to children, adults, and the developmental-ly disabled population...</p>
    <a class="btn is-active" href="#">More</a>
  </article>
  <article class="service-card" style="left:763px">
    <div class="service-photo" role="img" aria-label="Photo of a doctor examining a patient before a surgical consultation" style="background:linear-gradient(135deg,#cfd7de,#b39a86)"></div>
    <h3>Bariatric pre-surgical consultation</h3>
    <p>To provide mental health services to children, adults, and the developmental-ly disabled population...</p>
    <a class="btn" href="#">More</a>
  </article>
  <a class="btn btn-viewall" href="#">View All</a>
</section>

<section class="conditions">
  <div class="conditions-photo" role="img" aria-label="Photo of a worried woman sitting with her hand on her forehead"></div>
  <div class="conditions-body">
    <h2 class="section-heading">Conditions We Treat</h2>
    <ul class="condition-list">
      <li><svg width="24" height="24" viewBox="0 0 24 24"><circle cx="12" cy="12" r="10" fill="none" stroke="#fff" stroke-width="1.8"/><path d="M7 12.5l3.5 3.5L21 5" fill="none" stroke="#fff" stroke-width="2"/></svg>Mood Disorders</li>
      <li><svg width="24" height="24" viewBox="0 0 24 24"><circle cx="12" cy="12" r="10" fill="none" stroke="#fff" stroke-width="1.8"/><path d="M7 12.5l3.5 3.5L21 5" fill="none" stroke="#fff" stroke-width="2"/></svg>Anxiety Disorders</li>
      <li><svg width="24" height="24" viewBox="0 0 24 24"><circle cx="12" cy="12" r="10" fill="none" stroke="#fff" stroke-width="1.8"/><path d="M7 12.5l3.5 3.5L21 5" fill="none" stroke="#fff" stroke-width="2"/></svg>Common Disorders of Childhood</li>
      <li><svg width="24" height="24" viewBox="0 0 24 24"><circle cx="12" cy="12" r="10" fill="none" stroke="#fff" stroke-width="1.8"/><path d="M7 12.5l3.5 3.5L21 5" fill="none" stroke="#fff" stroke-width="2"/></svg>Psychotic Disorders</li>
    </ul>
    <a class="btn btn-conditions" href="#">More Conditions</a>
  </div>
</section>

<section class="news">
  <h2 class="section-heading block-heading" style="top:2020px">Latest News</h2>
  <div class="pager" style="left:991px;top:2024px">
    <span class="prev"><svg width="8" height="8" viewBox="0 0 8 8"><path d="M6 0 1 4l5 4z" fill="#1fb5d6"/></svg></span>
    <span class="next"><svg width="8" height="8" viewBox="0 0 8 8"><path d="M2 0l5 4-5 4z" fill="#fff"/></svg></span>
  </div>
  <article class="news-item" style="left:157px">
    <div class="news-photo" role="img" aria-label="Photo of a mother smiling with her child who uses a wheelchair outdoors" style="background:linear-gradient(135deg,#a9b98f,#6f8a5e)"></div>
    <p class="news-date">May 22, 2017</p>
    <h3 class="news-title">Contrary to popular belief, Lorem Ipsum is...</h3>
  </article>
  <article class="news-item" style="left:459px">
    <div class="news-photo" role="img" aria-label="Photo of a counselor taking notes while talking with a client" style="background:linear-gradient(135deg,#d9cbbd,#a4b48e)"></div>
    <p class="news-date">Jun 10, 2017</p>
    <h3 class="news-title">Contrary to popular belief, Lorem Ipsum is...</h3>
  </article>
  <article class="news-item" style="left:763px">
    <div class="news-photo" role="img" aria-label="Photo of a therapist helping an older man during a session" style="background:linear-gradient(135deg,#cdbfae,#8f8477)"></div>
    <p class="news-date">Sept 15, 2017</p>
    <h3 class="news-title is-hover">Contrary to popular belief, Lorem Ipsum is...</h3>
  </article>
  <a class="btn btn-news" href="#">View All</a>
</section>

<footer class="site-footer">
  <span class="footer-mark"></span>
  <div class="footer-contact">
    <h4>Maplecrest Behavioral Healthcare</h4>
    <p class="addr">418 Peachtree Ridge Rd, Fayetteville,<br>GA 30214</p>
    <h5>Contact Us</h5>
    <p class="phone">+1 404-555-0186</p>
    <p class="mail">hello@maplecrestbh.com</p>
    <p class="follow">Follow Us: <span></span></p>
  </div>
  <div class="quick-links">
    <h4>Quick Links</h4>
    <ul>
      <li class="is-current">Home</li>
      <li>About Us</li>
      <li>Services</li>
      <li>Conditions We Treat</li>
      <li>New Patients</li>
      <li>Contact</li>
    </ul>
  </div>
  <ul class="policy-links">
    <li>Privacy Policy</li>
    <li>Terms &amp; Conditions</li>
    <li>Treatment agreement</li>
    <li>Self report</li>
  </ul>
  <span class="badge"></span>
  <span class="footer-rule"></span>
  <div class="hours">
    <h4>Hours of Operation:</h4>
    <p>Closed on major Holidays and weekends<br>After Hours #s, Emergency Locations, Directions</p>
  </div>
  <span class="footer-bottom"></span>
  <p class="copyright">&copy; 2017 Maplecrest Behavioral Healthcare All Rights Reserved.</p>
  <svg class="to-top" width="18" height="26" viewBox="0 0 18 26"><path d="M9 25V3M2 10l7-8 7 8" fill="none" stroke="#4fb3e6" stroke-width="2"/></svg>
</footer>

</body>
</html>
```